Velmar Orthotics Promotional Brochure

We require a brochure to promote Velmar Orthotics manufacturing of custom foot orthotics to podiatrists. The design should have an active lifestyle and medical feel / look to it, clean and concise.

Ultimately the main point we want to get across is we make great orthotics in and industry leading turnaround time of 2 days! No other orthotic manufacturer can touch that.

I have attached some images for your use, but don't feel obligated to use them, please be creative and use what you like. THANKS!!

Deadline has been extended by 5 days. Thank-you.

```html
<!DOCTYPE html>
<html lang="en">
<head>
<meta charset="utf-8">
<title>Velmar Orthotics Brochure</title>
<link href="https://fonts.googleapis.com/css2?family=PT+Sans:wght@400;700&family=PT+Sans+Narrow:wght@700&display=swap" rel="stylesheet">
<style>
  :root {
    --brand-blue: #2f6fb3;
    --soft-blue: #5b95cf;
    --pale-blue: #cfe3f3;
    --ink: #1b1b1b;
    --paper: #ffffff;
    --stage: #e9ecef;
    --skin-light: #f6e2d4;
    --skin: #e8b898;
    --sky: #9cbfdc;
    --sky-deep: #5f8fbf;
    --grass: #3f7f6a;
  }
  html, body { margin: 0; padding: 0; overflow: hidden; }
  body {
    width: 1200px; height: 1000px;
    background: var(--stage);
    font-family: "PT Sans", Arial, sans-serif;
    color: var(--ink);
    position: relative;
  }
  .brochure {
    position: absolute; left: 30px; top: 60px;
    width: 990px; height: 765px;
    transform: scale(1.1515); transform-origin: 0 0;
    background: var(--paper);
    overflow: hidden;
    box-shadow: 0 4px 18px rgba(0,0,0,.18);
  }
  .abs { position: absolute; }

  /* left panel */
  .panel-title { left: 32px; top: 68px; font-size: 22px; line-height: 26px; color: var(--brand-blue); margin: 0; font-weight: 400; }
  .headline { left: 32px; top: 115px; font-size: 21px; line-height: 26px; margin: 0; font-weight: 400; }
  .question { left: 32px; top: 166px; font-size: 13.5px; line-height: 18px; font-weight: 700; margin: 0; }
  .body-copy { left: 32px; top: 202px; font-size: 13.5px; line-height: 18px; margin: 0; white-space: nowrap; }
  .body-copy p { margin: 0 0 18px; }
  .refill-lead { left: 32px; top: 446px; font-size: 13.5px; line-height: 18px; }
  .guarantee { left: 32px; top: 466px; font-size: 20px; line-height: 27px; color: var(--soft-blue); white-space: nowrap; }
  .seal { left: 30px; top: 592px; width: 116px; height: 116px; border-radius: 50%;
    background: radial-gradient(circle, var(--soft-blue) 0 58%, var(--brand-blue) 60%); }
  .photo-staff { left: 185px; top: 464px; width: 95px; height: 223px;
    background: linear-gradient(180deg, #eceef1 0%, #f7f7f8 55%, #3f3f44 56%, #2f2f34 100%);
    border-radius: 36px 36px 6px 6px; }

  /* middle panel */
  .photo-foot { left: 348px; top: 167px; width: 302px; height: 395px;
    background: radial-gradient(ellipse 60% 55% at 50% 48%, var(--skin) 0%, #edc5aa 45%, var(--skin-light) 75%, #fbf3ee 100%); }
  .mini-tagline { left: 376px; top: 94px; font-size: 17px; line-height: 23px; }
  .brand-mark { display: flex; align-items: center; gap: 8px; color: var(--ink); white-space: nowrap; }
  .brand-mark .dot { border-radius: 50%; background: var(--soft-blue); flex: none; }
  .brand-small { left: 445px; top: 531px; font-size: 13px; }
  .brand-small .dot { width: 32px; height: 32px; }
  .contact { left: 403px; font-size: 13px; line-height: 18px; display: flex; gap: 12px; align-items: flex-start; white-space: nowrap; }
  .contact svg { flex: none; }
  .contact-address { top: 586px; }
  .contact-phone { top: 650px; }
  .contact-email { top: 678px; }
  .contact-fax { top: 706px; }

  /* cover panel */
  .photo-runner { left: 650px; top: 142px; width: 340px; height: 530px;
    background: linear-gradient(180deg, #ffffff 0%, var(--sky) 16%, var(--sky-deep) 52%, #4f8a86 72%, var(--grass) 100%);
    -webkit-mask-image: linear-gradient(90deg, transparent 0, #000 60px);
            mask-image: linear-gradient(90deg, transparent 0, #000 60px); }
  .brand-large { left: 712px; top: 38px; font-size: 20px; }
  .brand-large .dot { width: 94px; height: 94px; }
  .cover-tagline { left: 682px; top: 351px; font-size: 29px; line-height: 39px; }
  .cover-phone { left: 710px; top: 686px; font-family: "PT Sans Narrow", "Arial Narrow", sans-serif; font-weight: 700; font-size: 35px; line-height: 40px; }

  .waves { left: 0; top: 560px; width: 990px; height: 205px; }
</style>
</head>
<body>
<main class="brochure">
  <div class="abs photo-foot" role="img" aria-label="Photo of hands examining a bare foot"></div>
  <div class="abs photo-runner" role="img" aria-label="Photo of a woman running through a grassy field holding a water bottle"></div>

  <svg class="abs waves" viewBox="0 0 990 205" aria-hidden="true">
    <defs>
      <linearGradient id="waveFade" x1="0" x2="1">
        <stop offset="0" stop-color="#cfe3f3" stop-opacity="0.3"/>
        <stop offset="0.6" stop-color="#a9cdea"/>
        <stop offset="1" stop-color="#5b95cf"/>
      </linearGradient>
    </defs>
    <path d="M0 130 C 250 100, 450 175, 700 150 S 900 70, 990 60 L990 205 L0 205 Z" fill="url(#waveFade)" opacity=".45"/>
    <path d="M0 175 C 250 150, 500 210, 760 180 S 940 120, 990 120 L990 205 L0 205 Z" fill="#cfe3f3" opacity=".8"/>
    <path d="M615 205 C 660 120, 790 78, 990 55 L990 92 C 840 98, 720 112, 660 205 Z" fill="#2f6fb3" opacity=".9"/>
    <path d="M0 196 C 300 182, 600 205, 990 150" fill="none" stroke="#5b95cf" stroke-width="2"/>
  </svg>

  <h2 class="abs panel-title">Main Message</h2>
  <h1 class="abs headline">2 day turnaround ….</h1>
  <p class="abs question">why is a 2 day turnaround important?</p>
  <div class="abs body-copy">
    <p>Early Intervention. …<br>The sooner your patients get their<br>prescribed orthotic treatment the sooner<br>they will improve. It has been well<br>documented that early intervention in<br>treatment protocols significantly<br>decreases the likelihood of a chronic issue<br>developing.!</p>
    <p>Utilizing our proprietary Cryo Mill<br>technology, in two days or less, we<br>achieve well balanced, accurate orthotics<br>with seamless FF transitions AND where</p>
  </div>
  <div class="abs refill-lead">refills are</div>
  <div class="abs guarantee">guaranteed<br>to be the<br>same as<br>originals.</div>
  <div class="abs seal" role="img" aria-label="Satisfaction guarantee seal"></div>
  <div class="abs photo-staff" role="img" aria-label="Photo of two clinicians in white coats"></div>

  <div class="abs mini-tagline">fit.<br>function.<br>finish ….<br>faster.</div>
  <div class="abs brand-mark brand-small"><span class="dot"></span>velmar orthotics</div>

  <div class="abs contact contact-address">
    <svg width="22" height="22" viewBox="0 0 22 22"><circle cx="11" cy="11" r="11" fill="#5b95cf"/><rect x="5" y="7" width="12" height="8" fill="#fff"/><path d="M5 7 L11 12 L17 7" fill="none" stroke="#5b95cf" stroke-width="1.2"/></svg>
    <span>Velmar Orthotics 214,<br>4120 - 52nd St NE Calgary,<br>AB T3J 0K6</span>
  </div>
  <div class="abs contact contact-phone">
    <svg width="22" height="22" viewBox="0 0 22 22"><circle cx="11" cy="11" r="11" fill="#5b95cf"/><path d="M6 9 Q11 5 16 9 L15 10 L13 9 L9 9 L7 10 Z M7 11 H15 V16 H7 Z" fill="#fff"/></svg>
    <span>1.403.555.0142</span>
  </div>
  <div class="abs contact contact-email">
    <svg width="22" height="22" viewBox="0 0 22 22"><circle cx="11" cy="11" r="11" fill="#5b95cf"/><text x="11" y="15.5" text-anchor="middle" font-size="13" fill="#fff" font-family="PT Sans, sans-serif">@</text></svg>
    <span>info@velmarorthotics.com</span>
  </div>
  <div class="abs contact contact-fax">
    <svg width="22" height="22" viewBox="0 0 22 22"><circle cx="11" cy="11" r="11" fill="#5b95cf"/><rect x="7" y="5" width="8" height="4" fill="#fff"/><rect x="5" y="10" width="12" height="5" fill="#fff"/><rect x="7" y="15" width="8" height="2" fill="#fff"/></svg>
    <span>1.888.555.0176</span>
  </div>

  <div class="abs brand-mark brand-large"><span class="dot"></span>velmar orthotics</div>
  <div class="abs cover-tagline">fit.<br>function.<br>finish ….<br>faster.</div>
  <div class="abs cover-phone">1.403.555.0142</div>
</main>
</body>
</html>
```